Redesign Video/PIcture Check in Page

Redesign our current TetherWatchApp iPhone App checkin screens - Keep the design simple so that programmers do not have to do too much extra work to make your design work. - Look at the attached website screenshot for the overall look and feel, and color scheme - Convert the attached vector logo to iOS Icon format. - Deliver all graphics in the density required for iPhone XS Max. I will upload current check in pages that need to be reimagined. Check in needs to be more intutitive. Would like to add some gamification to the verification screen where they currently are required to enter series of random numbers. simple card game etc might work better. See TetherWatchapp in itunes and google play store. also visit quorvant-link.example or tetherwatchapp.example for more information about our company.
The Current Checkin Process:
A. Client receives alert to checkin or submits voluntary checkin
B. Clicks checkin button on home Screen.
Redesign from here:
C. Clicks on a check in from check in list screen(new screen)
D. Enters verification number(gamification something better than random numbers)
E. Opens Camera
D. Takes Selfie
F. submits photo
G. clicks check in
SEE CURRENT STEPS PIC I UPLOADED

Target Market(s)

Courts,Probation and parole,Attorneys,Sheriffs,Jails, Alternative sentencing

Colors
3277b5

Requirements
Must have
• Must be easy to navigate,Intuitive!
Nice to have
• Gamification of check in verification.
• Step by step process with next button or similar

```html
<!DOCTYPE html>
<html lang="en">
<head>
<meta charset="utf-8">
<title>TetherWatchApp – Check-in Flow</title>
<link rel="stylesheet" href="https://fonts.googleapis.com/css2?family=Nunito+Sans:wght@400;600;700;800&display=swap">
<style>
  :root{
    --navy:#13306a;
    --navy-deep:#0e2a5f;
    --ink:#1c2a44;
    --muted:#9aa3b2;
    --soft:#b7bfcc;
    --field:#eef0f3;
    --panel:#f3f4f6;
    --line:#d9dde3;
    --white:#ffffff;
    --shadow:0 2px 6px rgba(20,30,60,.12);
  }
  *{box-sizing:border-box;margin:0;padding:0}
  html,body{width:1200px;height:1200px;overflow:hidden;background:var(--white)}
  body{font-family:"Nunito Sans",Arial,sans-serif;color:var(--ink)}
  .stage{position:absolute;left:0;top:0;width:1500px;height:1500px;transform:scale(.8);transform-origin:0 0}

  .screen{position:absolute;width:264px;height:636px;background:var(--white);box-shadow:var(--shadow);overflow:hidden}
  .statusbar{position:absolute;left:0;top:0;width:100%;height:20px}
  .statusbar .signal{position:absolute;left:6px;top:2px}
  .statusbar .clock{position:absolute;left:0;right:0;top:2px;text-align:center;font-size:8px;color:#555}
  .statusbar .battery{position:absolute;right:6px;top:2px}
  .menu-btn{position:absolute;left:0;top:40px}
  .close-btn{position:absolute;right:15px;top:43px}
  .screen-title{position:absolute;left:0;right:0;top:40px;text-align:center;font-size:18px;font-weight:600;color:var(--navy)}

  .stepper{position:absolute;left:0;top:70px;width:264px;height:40px}
  .stepper .rail{position:absolute;left:20px;right:20px;top:27px;height:1.5px;background:var(--navy)}
  .stepper .num{position:absolute;top:0;width:20px;margin-left:-10px;text-align:center;font-size:12px;color:var(--soft)}
  .stepper .num.on{color:var(--navy);font-weight:700}
  .stepper .dot{position:absolute;top:20px;width:16px;height:16px;margin-left:-8px;border-radius:50%;background:#dfe3e9;border:1.5px solid #c2c8d2}
  .stepper .dot.on{width:20px;height:20px;margin-left:-10px;top:18px;background:var(--navy);border:3px solid #fff;box-shadow:0 0 0 1.5px var(--navy)}

  .tabbar{position:absolute;left:0;bottom:0;width:100%;height:81px;background:var(--white)}
  .tab{position:absolute;top:14px;width:70px;margin-left:-35px;text-align:center;font-size:10px;color:var(--muted)}
  .tab svg{display:block;margin:0 auto 6px}
  .tab.on{color:#000;font-weight:600}
  .tab.on::after{content:"";display:block;width:52px;height:2px;background:#000;margin:4px auto 0}

  /* check-in list */
  .checkin-row{position:absolute;left:0;width:264px;height:68px}
  .checkin-row .date{position:absolute;left:0;top:0;width:60px;height:68px;background:var(--navy);color:#fff;text-align:center;padding-top:15px;line-height:1.15}
  .checkin-row .date .d{font-size:12px}
  .checkin-row .date .y{font-size:15px;font-weight:600}
  .checkin-row .body{position:absolute;left:60px;right:0;top:0;height:68px;background:var(--panel);border-bottom:1.5px solid var(--navy);padding:13px 0 0 7px}
  .checkin-row .title{font-size:13px;font-weight:700;color:var(--navy)}
  .checkin-row .time{font-size:12px;color:var(--soft);margin-top:3px}
  .checkin-row .box{position:absolute;right:14px;top:38px}

  /* court dates */
  .court-card{position:absolute;left:0;width:264px;background:var(--panel);border-bottom:1.5px solid var(--navy)}
  .court-card .bar{position:absolute;left:0;top:0;width:220px;height:27px;background:var(--navy);color:#fff;font-size:12.5px;font-weight:600;text-align:center;line-height:27px}
  .court-card .box{position:absolute;right:12px;top:6px}
  .court-card .info{position:absolute;left:8px;top:38px;font-size:10.5px;font-weight:700;color:var(--ink);line-height:1.35}
  .court-row{position:absolute;left:0;width:264px;background:var(--panel);border-bottom:1.5px solid var(--line)}
  .court-row .when{position:absolute;left:17px;top:26px;font-size:12.5px;color:#8d95a3}
  .court-row .box{position:absolute;right:12px;top:27px}

  /* check-in detail */
  .detail-bar{position:absolute;left:0;top:129px;width:264px;height:24px;background:var(--navy-deep);color:#fff;font-size:12.5px;font-weight:700;line-height:24px;padding:0 10px}
  .detail-bar span{float:right;font-weight:600}
  .detail-head{position:absolute;left:0;top:153px;width:264px;height:45px;background:var(--panel);padding:12px 6px;font-size:13px;font-weight:700;color:var(--navy)}
  .prompt{position:absolute;left:6px;top:206px;width:240px;font-size:14px;color:var(--muted);line-height:1.3}
  .code{position:absolute;left:0;right:0;top:245px;text-align:center;font-size:29px;font-weight:800;color:var(--navy)}
  .field{position:absolute;left:6px;width:249px;height:32px;background:var(--field);border:1px solid #dfe2e7;border-radius:3px;font-size:12px;color:#555;padding:0 12px;line-height:30px}
  .field.placeholder{color:var(--muted)}
  .field-label{position:absolute;left:6px;top:338px;font-size:14px;color:var(--muted)}
  .avatar{position:absolute;left:86px;top:410px;width:90px;height:90px;border-radius:50%;border:1.5px solid var(--navy);overflow:hidden;background:#fff}
  .avatar .photo{width:100%;height:100%;background:radial-gradient(circle at 50% 40%,#d8b49a 0 28%,#2b2f38 62%,#f4f4f4 63%)}
  .primary-btn{position:absolute;left:6px;top:518px;width:249px;height:32px;background:var(--navy-deep);color:#fff;border-radius:4px;font-size:12.5px;font-weight:600;text-align:center;line-height:32px}

  .dim{position:absolute;inset:0;background:rgba(40,40,40,.5)}
  .modal{position:absolute;left:15px;top:240px;width:230px;height:130px;background:#fff;border-radius:10px;text-align:center}
  .modal h2{font-size:20px;font-weight:600;color:var(--navy);margin-top:18px}
  .modal p{font-size:15px;color:var(--ink);margin-top:12px}
  .modal .ok{display:inline-block;margin-top:15px;width:64px;height:24px;background:var(--navy-deep);color:#fff;font-size:11px;line-height:24px;font-weight:600}

  /* camera */
  .camera{position:absolute;left:1008px;top:780px;width:300px;height:624px;background:#fff;box-shadow:var(--shadow);overflow:hidden}
  .camera .viewfinder{position:absolute;left:0;top:60px;width:300px;height:422px;background:linear-gradient(180deg,#f7f7f7 0%,#f1ede9 22%,#c79a7f 45%,#2d323d 72%,#1c2029 100%)}
  .camera .top-icon{position:absolute;top:16px}
  .camera .thumb{position:absolute;left:20px;top:514px;width:44px;height:44px;border-radius:4px;overflow:hidden;box-shadow:0 1px 3px rgba(0,0,0,.2)}
  .camera .thumb div{width:100%;height:100%;background:linear-gradient(180deg,#f2f2f2 0%,#caa58d 45%,#262a33 100%)}
  .camera .shutter{position:absolute;left:128px;top:510px}
  .camera .video{position:absolute;left:230px;top:522px}
  .camera .sysnav{position:absolute;top:582px}
</style>
</head>
<body>
<div class="stage">

  <!-- Screen 1: Check Ins list -->
  <section class="screen" style="left:192px;top:70px">
    <div class="statusbar">
      <svg class="signal" width="14" height="14" viewBox="0 0 14 14" fill="none" stroke="#333" stroke-width="1.6"><circle cx="3" cy="11" r="1.2" fill="#333" stroke="none"/><path d="M2 7a5 5 0 0 1 5 5M2 3a9 9 0 0 1 9 9"/></svg>
      <div class="clock">4:50 AM</div>
      <svg class="battery" width="20" height="10" viewBox="0 0 20 10"><rect x=".5" y=".5" width="17" height="9" fill="none" stroke="#333"/><rect x="2" y="2" width="14" height="6" fill="#333"/><rect x="18" y="3" width="1.5" height="4" fill="#333"/></svg>
    </div>
    <svg class="menu-btn" width="18" height="20" viewBox="0 0 18 20" fill="var(--navy)"><rect x="0" y="1" width="17" height="3"/><rect x="0" y="8.5" width="11" height="3"/><rect x="0" y="16" width="17" height="3"/></svg>
    <h1 class="screen-title">Check Ins</h1>
    <div class="stepper">
      <div class="rail"></div>
      <span class="num on" style="left:48px">1</span><span class="num" style="left:88px">2</span><span class="num" style="left:129px">3</span><span class="num" style="left:170px">4</span><span class="num" style="left:211px">5</span>
      <span class="dot on" style="left:48px"></span><span class="dot" style="left:88px"></span><span class="dot" style="left:129px"></span><span class="dot" style="left:170px"></span><span class="dot" style="left:211px"></span>
    </div>

    <div class="checkin-row" style="top:129px"><div class="date"><div class="d">20 oct</div><div class="y">2018</div></div><div class="body"><div class="title">Voluntary Check-in Request</div><div class="time">14.50.23</div><svg class="box" width="14" height="14" viewBox="0 0 14 14" fill="none" stroke="var(--navy)" stroke-width="1.3"><rect x=".7" y="1.5" width="12" height="12" rx="1"/><path d="M3.5 7l3 3 6.5-8.5"/></svg></div></div>
    <div class="checkin-row" style="top:204px"><div class="date"><div class="d">30 oct</div><div class="y">2018</div></div><div class="body"><div class="title">Voluntary Check-in Request</div><div class="time">14.50.23</div><svg class="box" width="14" height="14" viewBox="0 0 14 14" fill="none" stroke="var(--navy)" stroke-width="1.3"><rect x=".7" y="1.5" width="12" height="12" rx="1"/><path d="M3.5 7l3 3 6.5-8.5"/></svg></div></div>
    <div class="checkin-row" style="top:278px"><div class="date"><div class="d">30 oct</div><div class="y">2018</div></div><div class="body"><div class="title">Voluntary Check-in Request</div><div class="time">14.50.23</div><svg class="box" width="14" height="14" viewBox="0 0 14 14" fill="none" stroke="var(--navy)" stroke-width="1.3"><rect x=".7" y="1.5" width="12" height="12" rx="1"/></svg></div></div>
    <div class="checkin-row" style="top:353px"><div class="date"><div class="d">30 oct</div><div class="y">2018</div></div><div class="body"><div class="title">Voluntary Check-in Request</div><div class="time">14.50.23</div><svg class="box" width="14" height="14" viewBox="0 0 14 14" fill="none" stroke="var(--navy)" stroke-width="1.3"><rect x=".7" y="1.5" width="12" height="12" rx="1"/><path d="M3.5 7l3 3 6.5-8.5"/></svg></div></div>
    <div class="checkin-row" style="top:428px"><div class="date"><div class="d">30 oct</div><div class="y">2018</div></div><div class="body"><div class="title">Voluntary Check-in Request</div><div class="time">14.50.23</div><svg class="box" width="14" height="14" viewBox="0 0 14 14" fill="none" stroke="var(--navy)" stroke-width="1.3"><rect x=".7" y="1.5" width="12" height="12" rx="1"/></svg></div></div>
    <div class="checkin-row" style="top:502px"><div class="date"><div class="d">30 oct</div><div class="y">2018</div></div><div class="body"><div class="title">Voluntary Check-in Request</div><div class="time">14.50.23</div><svg class="box" width="14" height="14" viewBox="0 0 14 14" fill="none" stroke="var(--navy)" stroke-width="1.3"><rect x=".7" y="1.5" width="12" height="12" rx="1"/><path d="M3.5 7l3 3 6.5-8.5"/></svg></div></div>

    <nav class="tabbar">
      <div class="tab on" style="left:31px"><svg width="28" height="26" viewBox="0 0 28 26"><path d="M14 1L1 13h4v12h7v-8h4v8h7V13h4z" fill="#000"/></svg>Home</div>
      <div class="tab" style="left:104px"><svg width="22" height="26" viewBox="0 0 22 26" fill="none" stroke="var(--muted)" stroke-width="2.5"><path d="M11 24s-8-9-8-14a8 8 0 0 1 16 0c0 5-8 14-8 14z"/><circle cx="11" cy="10" r="2.5" fill="var(--muted)"/></svg>Check-ins (5)</div>
      <div class="tab" style="left:171px"><svg width="22" height="26" viewBox="0 0 22 26" fill="none" stroke="var(--muted)" stroke-width="2.5"><path d="M11 24s-8-9-8-14a8 8 0 0 1 16 0c0 5-8 14-8 14z"/><circle cx="11" cy="10" r="2.5" fill="var(--muted)"/></svg>Map</div>
      <div class="tab" style="left:234px"><svg width="26" height="26" viewBox="0 0 26 26" fill="none" stroke="var(--muted)" stroke-width="1.5"><circle cx="13" cy="13" r="11"/><path d="M13 11v8M13 7v1.5"/></svg>How to</div>
    </nav>
  </section>

  <!-- Screen 2: Court Dates -->
  <section class="screen" style="left:611px;top:80px">
    <div class="statusbar">
      <svg class="signal" width="14" height="14" viewBox="0 0 14 14" fill="none" stroke="#333" stroke-width="1.6"><circle cx="3" cy="11" r="1.2" fill="#333" stroke="none"/><path d="M2 7a5 5 0 0 1 5 5M2 3a9 9 0 0 1 9 9"/></svg>
      <div class="clock">4:50 AM</div>
      <svg class="battery" width="20" height="10" viewBox="0 0 20 10"><rect x=".5" y=".5" width="17" height="9" fill="none" stroke="#333"/><rect x="2" y="2" width="14" height="6" fill="#333"/><rect x="18" y="3" width="1.5" height="4" fill="#333"/></svg>
    </div>
    <svg class="menu-btn" width="18" height="20" viewBox="0 0 18 20" fill="var(--navy)"><rect x="0" y="1" width="17" height="3"/><rect x="0" y="8.5" width="11" height="3"/><rect x="0" y="16" width="17" height="3"/></svg>
    <h1 class="screen-title">Court Dates</h1>
    <div class="stepper">
      <div class="rail"></div>
      <span class="num" style="left:48px">1</span><span class="num on" style="left:88px">2</span><span class="num" style="left:129px">3</span><span class="num" style="left:170px">4</span><span class="num" style="left:211px">5</span>
      <span class="dot" style="left:48px"></span><span class="dot on" style="left:88px"></span><span class="dot" style="left:129px"></span><span class="dot" style="left:170px"></span><span class="dot" style="left:211px"></span>
    </div>

    <div class="court-card" style="top:130px;height:78px"><div class="bar">30 oct 2018 14.50.23</div><svg class="box" width="14" height="14" viewBox="0 0 14 14" fill="none" stroke="var(--navy)" stroke-width="1.3"><rect x=".7" y="1.5" width="12" height="12" rx="1"/><path d="M3.5 7l3 3 6.5-8.5"/></svg><div class="info">Court date Friday the 13th at 9.00 a.m.<br>Maplewood County Circuit Court Room 105</div></div>
    <div class="court-card" style="top:214px;height:80px"><div class="bar">30 oct 2018 14.50.23</div><svg class="box" width="14" height="14" viewBox="0 0 14 14" fill="none" stroke="var(--navy)" stroke-width="1.3"><rect x=".7" y="1.5" width="12" height="12" rx="1"/><path d="M3.5 7l3 3 6.5-8.5"/></svg><div class="info">Thursday September 3rd,2018 at 1.00 p.m.<br>Ridgefield District Court</div></div>
    <div class="court-card" style="top:298px;height:82px"><div class="bar">30 oct 2018 14.50.23</div><svg class="box" width="14" height="14" viewBox="0 0 14 14" fill="none" stroke="var(--navy)" stroke-width="1.3"><rect x=".7" y="1.5" width="12" height="12" rx="1"/></svg><div class="info" style="left:11px">Monday July 4th,2018 at 9.00 a.m.<br>Maplewood County Circuit Court Room 105</div></div>
    <div class="court-row" style="top:384px;height:68px"><div class="when">30 oct 2018 14.50.23</div><svg class="box" width="14" height="14" viewBox="0 0 14 14" fill="none" stroke="var(--navy)" stroke-width="1.3"><rect x=".7" y="1.5" width="12" height="12" rx="1"/><path d="M3.5 7l3 3 6.5-8.5"/></svg></div>
    <div class="court-row" style="top:456px;height:68px"><div class="when">30 oct 2018 14.50.23</div><svg class="box" width="14" height="14" viewBox="0 0 14 14" fill="none" stroke="var(--navy)" stroke-width="1.3"><rect x=".7" y="1.5" width="12" height="12" rx="1"/><path d="M3.5 7l3 3 6.5-8.5"/></svg></div>
    <div class="court-row" style="top:528px;height:68px"><div class="when">30 oct 2018 14.50.23</div></div>

    <nav class="tabbar">
      <div class="tab on" style="left:31px"><svg width="28" height="26" viewBox="0 0 28 26"><path d="M14 1L1 13h4v12h7v-8h4v8h7V13h4z" fill="#000"/></svg>Home</div>
      <div class="tab" style="left:100px"><svg width="22" height="26" viewBox="0 0 22 26" fill="none" stroke="var(--muted)" stroke-width="2.5"><path d="M11 24s-8-9-8-14a8 8 0 0 1 16 0c0 5-8 14-8 14z"/><circle cx="11" cy="10" r="2.5" fill="var(--muted)"/></svg>Check-ins (5)</div>
      <div class="tab" style="left:171px"><svg width="22" height="26" viewBox="0 0 22 26" fill="none" stroke="var(--muted)" stroke-width="2.5"><path d="M11 24s-8-9-8-14a8 8 0 0 1 16 0c0 5-8 14-8 14z"/><circle cx="11" cy="10" r="2.5" fill="var(--muted)"/></svg>Map</div>
      <div class="tab" style="left:233px"><svg width="26" height="26" viewBox="0 0 26 26" fill="none" stroke="var(--muted)" stroke-width="1.5"><circle cx="13" cy="13" r="11"/><path d="M13 11v8M13 7v1.5"/></svg>How to</div>
    </nav>
  </section>

  <!-- Screen 3: Check In, no photo yet -->
  <section class="screen" style="left:1053px;top:70px">
    <div class="statusbar">
      <svg class="signal" width="14" height="14" viewBox="0 0 14 14" fill="none" stroke="#333" stroke-width="1.6"><circle cx="3" cy="11" r="1.2" fill="#333" stroke="none"/><path d="M2 7a5 5 0 0 1 5 5M2 3a9 9 0 0 1 9 9"/></svg>
      <div class="clock">4:50 AM</div>
      <svg class="battery" width="20" height="10" viewBox="0 0 20 10"><rect x=".5" y=".5" width="17" height="9" fill="none" stroke="#333"/><rect x="2" y="2" width="14" height="6" fill="#333"/><rect x="18" y="3" width="1.5" height="4" fill="#333"/></svg>
    </div>
    <h1 class="screen-title">Check In</h1>
    <div class="stepper">
      <div class="rail"></div>
      <span class="num" style="left:48px">1</span><span class="num" style="left:88px">2</span><span class="num on" style="left:129px">3</span><span class="num" style="left:170px">4</span><span class="num" style="left:211px">5</span>
      <span class="dot" style="left:48px"></span><span class="dot" style="left:88px"></span><span class="dot on" style="left:129px"></span><span class="dot" style="left:170px"></span><span class="dot" style="left:211px"></span>
    </div>
    <div class="detail-bar">20 oct 2018<span>14.50.23</span></div>
    <div class="detail-head">Voluntary Check-in Request</div>
    <p class="prompt">Please Check-in and Quote this number :</p>
    <div class="code">9BKU</div>
    <div class="field" style="top:301px">9BKU</div>
    <div class="field-label">Comment</div>
    <div class="field placeholder" style="top:364px">Type your reply</div>
    <div class="avatar">
      <svg width="90" height="90" viewBox="0 0 90 90"><circle cx="45" cy="31" r="15" fill="#9a9a9a"/><path d="M16 72c0-14 13-22 29-22s29 8 29 22v4H16z" fill="#9a9a9a"/></svg>
    </div>
    <div class="primary-btn">Check-In</div>
    <nav class="tabbar">
      <div class="tab on" style="left:31px"><svg width="28" height="26" viewBox="0 0 28 26"><path d="M14 1L1 13h4v12h7v-8h4v8h7V13h4z" fill="#000"/></svg>Home</div>
      <div class="tab" style="left:101px"><svg width="22" height="26" viewBox="0 0 22 26" fill="none" stroke="var(--muted)" stroke-width="2.5"><path d="M11 24s-8-9-8-14a8 8 0 0 1 16 0c0 5-8 14-8 14z"/><circle cx="11" cy="10" r="2.5" fill="var(--muted)"/></svg>Check-ins (5)</div>
      <div class="tab" style="left:171px"><svg width="22" height="26" viewBox="0 0 22 26" fill="none" stroke="var(--muted)" stroke-width="2.5"><path d="M11 24s-8-9-8-14a8 8 0 0 1 16 0c0 5-8 14-8 14z"/><circle cx="11" cy="10" r="2.5" fill="var(--muted)"/></svg>Map</div>
      <div class="tab" style="left:233px"><svg width="26" height="26" viewBox="0 0 26 26" fill="none" stroke="var(--muted)" stroke-width="1.5"><circle cx="13" cy="13" r="11"/><path d="M13 11v8M13 7v1.5"/></svg>How to</div>
    </nav>
  </section>

  <!-- Screen 4: Check In with selfie -->
  <section class="screen" style="left:192px;top:778px;width:262px;height:632px">
    <div class="statusbar">
      <svg class="signal" width="14" height="14" viewBox="0 0 14 14" fill="none" stroke="#333" stroke-width="1.6"><circle cx="3" cy="11" r="1.2" fill="#333" stroke="none"/><path d="M2 7a5 5 0 0 1 5 5M2 3a9 9 0 0 1 9 9"/></svg>
      <div class="clock">4:50 AM</div>
      <svg class="battery" width="20" height="10" viewBox="0 0 20 10"><rect x=".5" y=".5" width="17" height="9" fill="none" stroke="#333"/><rect x="2" y="2" width="14" height="6" fill="#333"/><rect x="18" y="3" width="1.5" height="4" fill="#333"/></svg>
    </div>
    <h1 class="screen-title">Check In</h1>
    <svg class="close-btn" width="18" height="18" viewBox="0 0 18 18" fill="none" stroke="var(--navy)" stroke-width="1.3"><circle cx="9" cy="9" r="8"/><path d="M6 6l6 6M12 6l-6 6"/></svg>
    <div class="stepper">
      <div class="rail"></div>
      <span class="num" style="left:47px">1</span><span class="num" style="left:88px">2</span><span class="num" style="left:128px">3</span><span class="num on" style="left:169px">4</span><span class="num" style="left:210px">5</span>
      <span class="dot" style="left:47px"></span><span class="dot" style="left:88px"></span><span class="dot" style="left:128px"></span><span class="dot on" style="left:169px"></span><span class="dot" style="left:210px"></span>
    </div>
    <div class="detail-bar" style="width:262px">20 oct 2018<span>14.50.23</span></div>
    <div class="detail-head" style="width:262px">Voluntary Check-in Request</div>
    <p class="prompt">Please Check-in and Quote this number :</p>
    <div class="code">9BKU</div>
    <div class="field" style="top:299px;width:247px">9BKU</div>
    <div class="field-label" style="top:336px">Comment</div>
    <div class="field placeholder" style="top:362px;width:247px">Type your reply</div>
    <div class="avatar" style="left:85px;top:408px"><div class="photo" role="img" aria-label="Submitted selfie of the client"></div></div>
    <div class="primary-btn" style="top:515px;width:247px">Check-In</div>
    <nav class="tabbar">
      <div class="tab on" style="left:31px"><svg width="28" height="26" viewBox="0 0 28 26"><path d="M14 1L1 13h4v12h7v-8h4v8h7V13h4z" fill="#000"/></svg>Home</div>
      <div class="tab" style="left:100px"><svg width="22" height="26" viewBox="0 0 22 26" fill="none" stroke="var(--muted)" stroke-width="2.5"><path d="M11 24s-8-9-8-14a8 8 0 0 1 16 0c0 5-8 14-8 14z"/><circle cx="11" cy="10" r="2.5" fill="var(--muted)"/></svg>Check-ins (5)</div>
      <div class="tab" style="left:170px"><svg width="22" height="26" viewBox="0 0 22 26" fill="none" stroke="var(--muted)" stroke-width="2.5"><path d="M11 24s-8-9-8-14a8 8 0 0 1 16 0c0 5-8 14-8 14z"/><circle cx="11" cy="10" r="2.5" fill="var(--muted)"/></svg>Map</div>
      <div class="tab" style="left:232px"><svg width="26" height="26" viewBox="0 0 26 26" fill="none" stroke="var(--muted)" stroke-width="1.5"><circle cx="13" cy="13" r="11"/><path d="M13 11v8M13 7v1.5"/></svg>How to</div>
    </nav>
  </section>

  <!-- Screen 5: Success dialog -->
  <section class="screen" style="left:602px;top:778px;width:260px;height:628px">
    <div class="statusbar">
      <svg class="signal" width="14" height="14" viewBox="0 0 14 14" fill="none" stroke="#333" stroke-width="1.6"><circle cx="3" cy="11" r="1.2" fill="#333" stroke="none"/><path d="M2 7a5 5 0 0 1 5 5M2 3a9 9 0 0 1 9 9"/></svg>
      <div class="clock">4:50 AM</div>
      <svg class="battery" width="20" height="10" viewBox="0 0 20 10"><rect x=".5" y=".5" width="17" height="9" fill="none" stroke="#333"/><rect x="2" y="2" width="14" height="6" fill="#333"/><rect x="18" y="3" width="1.5" height="4" fill="#333"/></svg>
    </div>
    <h1 class="screen-title">Check In</h1>
    <svg class="close-btn" width="18" height="18" viewBox="0 0 18 18" fill="none" stroke="var(--navy)" stroke-width="1.3"><circle cx="9" cy="9" r="8"/><path d="M6 6l6 6M12 6l-6 6"/></svg>
    <div class="stepper">
      <div class="rail"></div>
      <span class="num" style="left:47px">1</span><span class="num" style="left:87px">2</span><span class="num" style="left:128px">3</span><span class="num" style="left:168px">4</span><span class="num on" style="left:208px">5</span>
      <span class="dot" style="left:47px"></span><span class="dot" style="left:87px"></span><span class="dot" style="left:128px"></span><span class="dot" style="left:168px"></span><span class="dot on" style="left:208px"></span>
    </div>
    <div class="detail-bar" style="width:260px">20 oct 2018<span>14.50.23</span></div>
    <div class="detail-head" style="width:260px">Voluntary Check-in Request</div>
    <p class="prompt">Please Check-in and Quote this number :</p>
    <div class="field" style="top:298px;width:245px">9BKU</div>
    <div class="field placeholder" style="top:359px;width:245px">Type your reply</div>
    <div class="avatar" style="left:84px;top:406px"><div class="photo" role="img" aria-label="Submitted selfie of the client"></div></div>
    <div class="primary-btn" style="top:512px;width:245px">Check-In</div>
    <nav class="tabbar" style="height:84px">
      <div class="tab on" style="left:31px"><svg width="28" height="26" viewBox="0 0 28 26"><path d="M14 1L1 13h4v12h7v-8h4v8h7V13h4z" fill="#000"/></svg>Home</div>
      <div class="tab" style="left:100px"><svg width="22" height="26" viewBox="0 0 22 26" fill="none" stroke="var(--muted)" stroke-width="2.5"><path d="M11 24s-8-9-8-14a8 8 0 0 1 16 0c0 5-8 14-8 14z"/><circle cx="11" cy="10" r="2.5" fill="var(--muted)"/></svg>Check-ins (5)</div>
      <div class="tab" style="left:168px"><svg width="22" height="26" viewBox="0 0 22 26" fill="none" stroke="var(--muted)" stroke-width="2.5"><path d="M11 24s-8-9-8-14a8 8 0 0 1 16 0c0 5-8 14-8 14z"/><circle cx="11" cy="10" r="2.5" fill="var(--muted)"/></svg>Map</div>
      <div class="tab" style="left:230px"><svg width="26" height="26" viewBox="0 0 26 26" fill="none" stroke="var(--muted)" stroke-width="1.5"><circle cx="13" cy="13" r="11"/><path d="M13 11v8M13 7v1.5"/></svg>How to</div>
    </nav>
    <div class="dim" style="top:20px"></div>
    <div class="modal">
      <h2>success!</h2>
      <p>Check-in Complete</p>
      <div class="ok">OK</div>
    </div>
  </section>

  <!-- Screen 6: Selfie camera -->
  <section class="camera">
    <svg class="top-icon" style="left:14px" width="28" height="28" viewBox="0 0 28 28" fill="none" stroke="var(--navy)" stroke-width="1.5"><circle cx="14" cy="14" r="12.5"/><circle cx="14" cy="14" r="6" stroke-width="3.5" stroke-dasharray="3 1.7"/><circle cx="14" cy="14" r="2.2" fill="var(--navy)"/></svg>
    <svg class="top-icon" style="left:256px" width="30" height="30" viewBox="0 0 30 30" fill="none" stroke="var(--navy)" stroke-width="1.5"><circle cx="15" cy="15" r="13.5"/><rect x="8" y="10" width="14" height="10" rx="1.5" fill="var(--navy)" stroke="none"/><rect x="12" y="8" width="6" height="3" fill="var(--navy)" stroke="none"/><circle cx="15" cy="15" r="3" fill="#fff" stroke="none"/></svg>
    <div class="viewfinder" role="img" aria-label="Live camera preview of the client taking a selfie"></div>
    <div class="thumb"><div role="img" aria-label="Last captured selfie"></div></div>
    <svg class="shutter" width="44" height="44" viewBox="0 0 44 44"><circle cx="22" cy="22" r="20" fill="none" stroke="var(--navy)" stroke-width="2"/><circle cx="22" cy="22" r="15" fill="var(--navy)"/></svg>
    <svg class="video" width="28" height="20" viewBox="0 0 28 20" fill="var(--navy)"><circle cx="6" cy="5" r="4"/><circle cx="14" cy="5" r="4"/><rect x="1" y="8" width="18" height="11" rx="1.5"/><path d="M19 12l8-5v12l-8-5z"/></svg>
    <svg class="sysnav" style="left:16px" width="14" height="12" viewBox="0 0 14 12" fill="var(--navy)"><rect y="1" width="14" height="2"/><rect y="5" width="14" height="2"/><rect y="9" width="14" height="2"/></svg>
    <svg class="sysnav" style="left:143px" width="16" height="14" viewBox="0 0 16 14" fill="none" stroke="var(--navy)" stroke-width="1.4"><rect x="1" y="1" width="14" height="12"/></svg>
    <svg class="sysnav" style="left:269px" width="18" height="16" viewBox="0 0 18 16" fill="none" stroke="var(--navy)" stroke-width="1.4"><path d="M16 1L2 8l14 7z"/></svg>
  </section>

</div>
</body>
</html>
```